TRIVAN 2026 Flyer for Conference

TRIVAN needs a design for a 1-page flyer that we will hand out at an upcoming event & then later post online as a pdf. There are 3 elements which need to be on the flyer:

1) A logo. This should be prominent on the design (e.g., in the middle). The flyer should use the colors that are in that logo (e.g., for accents, design elements, and/or text; not all of these have to be used):
Dark blue: #185577
Med blue: #327C9A
Teal: #4EB1C2
Light Teal: #9EDBE6

2) The conference theme -- Forests of Wonder: Climbing toward Research Fluency -- should be at the flyer's top.

3) Finally, these six tracks should be listed below the theme and the logo (it's font size should be at least a couple sizes smaller than the size used for the theme):
- Pearls of Pedagogy: Teaching Techniques that Work
- The Depth Gauge: Measuring Instructional Impact
- Techtonic Shifts: Innovation and Educational Technology
- Captain's Log: Navigating Leadership in Library Instruction
- Swimming Together: Collaborating with Others
- The Bermuda Triangle: Exploring (Seemingly) Eternal Challenges

Font styles to use
Sans Serif

Colors
0094D4
00A9DD
6FCCEA
C7EBF8
E9F6FB

Requirements
Must have
• The 3 elements listed in the description: 1) the logo, 2) the text of the theme and 3) the text for the tracks.

```html
<!DOCTYPE html>
<html lang="en">
<head>
<meta charset="utf-8">
<title>TRIVAN 2026 Conference Flyer</title>
<link href="https://fonts.googleapis.com/css2?family=Montserrat:wght@300;500;600;700;800&display=swap" rel="stylesheet">
<style>
  :root {
    --dark-blue: #185577;
    --med-blue: #327C9A;
    --teal: #4EB1C2;
    --light-teal: #9EDBE6;
    --ink: #111111;
    --paper: #ffffff;
  }
  * { margin: 0; padding: 0; box-sizing: border-box; }
  html, body { width: 770px; height: 1200px; overflow: hidden; background: var(--paper); }
  body { font-family: "Montserrat", Arial, sans-serif; color: var(--ink); }
  .flyer { position: relative; width: 770px; height: 1200px; background: var(--paper); }

  .logo-block { position: absolute; left: 0; top: 40px; width: 770px; height: 540px; }
  .logo-block svg { display: block; }
  .logo-name { font-family: "Montserrat", Arial, sans-serif; font-weight: 800; fill: var(--dark-blue); }
  .logo-year { font-family: "Montserrat", Arial, sans-serif; font-weight: 700; fill: var(--teal); }
  .logo-place { font-family: "Montserrat", Arial, sans-serif; font-weight: 500; fill: var(--teal); letter-spacing: 5px; }

  .theme-lead {
    position: absolute; top: 594px; left: 0; width: 770px;
    text-align: center; font-weight: 700; font-size: 34px; letter-spacing: 0.5px;
  }
  .theme-band {
    position: absolute; top: 645px; left: 0; width: 770px; height: 176px;
    background: var(--dark-blue); color: var(--paper); text-align: center;
    display: flex; flex-direction: column; justify-content: center;
  }
  .theme-band .light { font-weight: 300; font-size: 44px; line-height: 1.15; letter-spacing: 1px; }
  .theme-band .bold { font-weight: 800; font-size: 44px; line-height: 1.15; letter-spacing: 0.5px; }

  .tracks {
    position: absolute; top: 842px; left: 44px; width: 700px;
    display: grid; grid-template-columns: 338px 362px; row-gap: 18px;
  }
  .track { display: flex; align-items: flex-start; height: 84px; }
  .track-icon {
    flex: 0 0 72px; width: 72px; height: 72px; border-radius: 50%;
    border: 3px solid var(--teal); display: flex; align-items: center; justify-content: center;
    margin-right: 8px;
  }
  .track-icon svg { width: 38px; height: 38px; stroke: var(--ink); fill: none; stroke-width: 2; stroke-linecap: round; stroke-linejoin: round; }
  .track-text { padding-top: 6px; }
  .track-title { color: var(--med-blue); font-weight: 700; font-size: 18px; line-height: 1.1; }
  .track-desc { font-weight: 600; font-size: 15.5px; line-height: 1.13; margin-top: 3px; }

  .footer-band { position: absolute; left: 0; bottom: 0; width: 770px; height: 42px; background: var(--dark-blue); }
</style>
</head>
<body>
<main class="flyer">
  <section class="logo-block">
    <svg width="770" height="540" viewBox="0 0 770 540" aria-label="TRIVAN 2026, Bayport, VA, May 7-9">
      <defs>
        <path id="place-arc" d="M 150 380 Q 385 560 620 380"/>
      </defs>
      <circle cx="92" cy="300" r="38" fill="var(--light-teal)"/>
      <text class="logo-name" x="148" y="342" font-size="110" textLength="472" lengthAdjust="spacingAndGlyphs">TRIVAN</text>
      <text class="logo-year" x="634" y="334" font-size="44" textLength="108" lengthAdjust="spacingAndGlyphs">2026</text>
      <text class="logo-place" font-size="30">
        <textPath href="#place-arc" startOffset="50%" text-anchor="middle">BAYPORT, VA · MAY 7-9</textPath>
      </text>
    </svg>
  </section>

  <h1 class="theme-lead">FORESTS OF WONDER:</h1>
  <div class="theme-band">
    <div class="light">CLIMBING TOWARD</div>
    <div class="bold">RESEARCH FLUENCY</div>
  </div>

  <section class="tracks">
    <div class="track">
      <div class="track-icon"><svg viewBox="0 0 40 40"><circle cx="10" cy="9" r="4"/><path d="M10 14v14M6 18v10M14 18v10M10 28v8M14 20l8-6"/><rect x="20" y="5" width="16" height="11"/></svg></div>
      <div class="track-text"><div class="track-title">Pearls of Pedagogy:</div><div class="track-desc">Teaching Techniques<br>that Work</div></div>
    </div>
    <div class="track">
      <div class="track-icon"><svg viewBox="0 0 40 40"><circle cx="20" cy="8" r="4"/><path d="M20 12v4M12 10l-3-3M28 10l3-3M12 22c0-6 4-8 8-8s8 2 8 8v6H12z"/><path d="M16 20v6M20 20v6M24 20v6M14 28v6h12v-6"/></svg></div>
      <div class="track-text"><div class="track-title">Captain's Log:</div><div class="track-desc">Navigating Leadership in<br>Library Instruction</div></div>
    </div>
    <div class="track">
      <div class="track-icon"><svg viewBox="0 0 40 40"><path d="M6 34L6 6L34 34Z"/><path d="M11 29V19L21 29Z"/><path d="M6 12h3M6 18h3M6 24h3M12 34v-3M18 34v-3M24 34v-3"/></svg></div>
      <div class="track-text"><div class="track-title">The Depth Gauge:</div><div class="track-desc">Measuring<br>Instructional Impact</div></div>
    </div>
    <div class="track">
      <div class="track-icon"><svg viewBox="0 0 40 40"><path d="M4 26l8-10 6 4 4-4 6 4 8 8M12 16l6 6 4-2M18 20l6 6M8 28l4 6M28 28l4 6"/><path d="M20 4v3M12 7l2 2M28 7l-2 2"/></svg></div>
      <div class="track-text"><div class="track-title">Swimming Together:</div><div class="track-desc">Collaborating with Others</div></div>
    </div>
    <div class="track">
      <div class="track-icon"><svg viewBox="0 0 40 40"><circle cx="20" cy="13" r="6"/><path d="M17 19v3h6v-3M18 25h4M20 3v2M10 7l2 2M30 7l-2 2M6 26c2 4 6 8 12 8M34 26c-2 4-6 8-12 8M6 26v-6M34 26v-6"/></svg></div>
      <div class="track-text"><div class="track-title">Techtonic Shifts:</div><div class="track-desc">Innovation and<br>Educational Technology</div></div>
    </div>
    <div class="track">
      <div class="track-icon"><svg viewBox="0 0 40 40"><rect x="16" y="5" width="18" height="24"/><circle cx="10" cy="12" r="5"/><path d="M10 7v5h5M4 34V24M9 34V20M14 34V26M20 14h10M20 19h6"/><circle cx="26" cy="26" r="5"/><path d="M30 30l5 5"/></svg></div>
      <div class="track-text"><div class="track-title">The Bermuda Triangle:</div><div class="track-desc">Exploring (Seemingly)<br>Eternal Challenges</div></div>
    </div>
  </section>

  <div class="footer-band"></div>
</main>
</body>
</html>
```